Modern Business Card For A Digital Advertising Company

I'll be print on the Tarn Prints Velour paper http://us.tarnprints.example/products/velour/business-cards.html
Need's to be modern and use the color palette of the logo or gray scales. I think integrating the pixelation of the logo in to the card and having it wrap from one side to the other could be interesting. My company provides ad operations, web development, and number of other services to websites around the world. You can see my website at http://www.pixelharbor.example
Contact info on the card needs to have
Dana Welloby
President
p.555.318.4406
dana@pixelharbor.example
http://www.pixelharbor.example
Doesn't necessarily need to be in that order
Target Market(s)
Website owners
Industry/Entity Type
Business
Look and feel

```html
<!DOCTYPE html>
<html lang="en">
<head>
<meta charset="utf-8">
<title>Pixel Harbor – Business Card</title>
<link href="https://fonts.googleapis.com/css2?family=Roboto+Condensed:wght@400;700&display=swap" rel="stylesheet">
<style>
  :root {
    --stage: #2a2a2a;
    --card: #ffffff;
    --ink: #3a3a3a;
    --ink-soft: #5a5a5a;
    --green: #8dc63f;
    --pixel-grey: #d9d9d9;
  }
  * { box-sizing: border-box; margin: 0; padding: 0; }
  html, body {
    width: 1200px;
    height: 1000px;
    overflow: hidden;
    background: var(--stage);
    font-family: "Roboto Condensed", "Arial Narrow", sans-serif;
  }
  .card {
    position: absolute;
    left: 365px;
    top: 90px;
    width: 470px;
    height: 820px;
    background: var(--card);
  }
  .pixel-field {
    position: absolute;
    background: var(--pixel-grey);
  }
  .pixel-field--top { left: 190px; top: 0; width: 50px; height: 80px; }
  .pixel-field--bottom { left: 70px; top: 770px; width: 200px; height: 50px; opacity: .8; }

  .identity { position: absolute; left: 268px; top: 24px; }
  .identity__name { font-size: 28px; font-weight: 700; color: var(--ink); line-height: 1.25; }
  .identity__role { font-size: 28px; font-weight: 400; color: var(--green); line-height: 1.25; }

  .brand {
    position: absolute;
    left: 96px;
    top: 250px;
    display: flex;
    align-items: flex-start;
    gap: 18px;
  }
  .brand__mark { width: 40px; height: 40px; background: var(--green); margin-top: 14px; }
  .brand__name {
    font-size: 76px;
    font-weight: 700;
    color: var(--green);
    line-height: .95;
    text-transform: uppercase;
  }

  .website {
    position: absolute;
    left: 26px;
    bottom: 80px;
    writing-mode: vertical-rl;
    transform: rotate(180deg);
    font-size: 19px;
    letter-spacing: 4px;
    color: var(--ink-soft);
  }

  .contact { position: absolute; left: 72px; top: 676px; font-size: 27px; line-height: 1.35; }
  .contact__phone { color: var(--ink); }
  .contact__phone b { font-weight: 700; }
  .contact__email { color: var(--green); }
</style>
</head>
<body>
  <main class="card">
    <div class="pixel-field pixel-field--top" role="img" aria-label="Grey pixel cluster decoration"></div>

    <header class="identity">
      <p class="identity__name">Dana Welloby</p>
      <p class="identity__role">President</p>
    </header>

    <div class="brand">
      <span class="brand__mark"></span>
      <p class="brand__name">Pixel<br>Harbor</p>
    </div>

    <p class="website">www.pixelharbor.example</p>

    <address class="contact" style="font-style:normal">
      <p class="contact__phone">P. <b>555.318.4406</b></p>
      <p class="contact__email">dana@pixelharbor.example</p>
    </address>

    <div class="pixel-field pixel-field--bottom" role="img" aria-label="Grey pixel cluster decoration"></div>
  </main>
</body>
</html>
```